Commercial Waterproofing Modern Business Cards

We are a Commercial Waterproofing company. We do a variety of jobs on the exterior of buildings. We repel from the top or scaffold to reach the areas. Cut out and recaulk expansion joints and apply sealants, brick/concrete repairs, seal window frame perimeters, and much more. Our website is www.ledgecrestfix.com.
We are looking for a new business card design that would look more modern and cutting edge. We like the transparent paper and had thought about using our logo, but maybe pulling it apart to where the building part is kind of in the background. I have attached 2 different logos that we use regularly. We want the design to be a little funky, but professional at the same time. We really don't want the logo to be incorporated by itself, but you can use the logo and take out the buildings and just use the name or vice versa. Please don't just put the logo on the card and the words around that.

Target Market(s)

Property Managers/Building Maintenance

Industry/Entity Type

Business

Contact Information for Business Card

Daniel Trovato President
Office (919)555-4827
Mobile (919)555-9306

Font styles to use
Serif

Requirements
Must have
• Nice overall design, somehow pulling from the logo for the design
Nice to have
• Look artsy and modern with a nice quality paper
Should not have
• Too many words or distracting designs. The logo 'as is'

```html
<!DOCTYPE html>
<html lang="en">
<head>
<meta charset="utf-8">
<title>Ledgecrest Fix – Business Card</title>
<link rel="stylesheet" href="https://fonts.googleapis.com/css2?family=Lato:wght@300;400;700;900&display=swap">
<style>
  :root {
    --backdrop: #3b3b3b;
    --card-blue: #34659a;
    --card-black: #070707;
    --card-cream: #e6d9a6;
    --ink-cream: #f2e6b3;
    --ink-white: #ffffff;
  }
  * { margin: 0; padding: 0; box-sizing: border-box; }
  html, body {
    width: 1200px;
    height: 900px;
    overflow: hidden;
    background: var(--backdrop);
    font-family: "Lato", Arial, sans-serif;
  }
  .stage {
    width: 1200px;
    height: 900px;
    display: flex;
    align-items: center;
    justify-content: center;
  }
  .business-card {
    position: relative;
    width: 1050px;
    height: 600px;
    background: var(--card-blue);
    overflow: hidden;
  }
  .card-shapes {
    position: absolute;
    inset: 0;
    width: 100%;
    height: 100%;
  }
  .shape-black { fill: var(--card-black); }
  .shape-cream { fill: var(--card-cream); }

  .brand-name {
    position: absolute;
    left: 90px;
    top: 330px;
    width: 400px;
    text-align: center;
    color: var(--ink-cream);
    font-weight: 900;
    font-size: 64px;
    line-height: 1;
    letter-spacing: 1px;
  }

  .contact-block {
    position: absolute;
    right: 75px;
    top: 78px;
    text-align: right;
    color: var(--ink-cream);
  }
  .person-name {
    font-size: 40px;
    font-weight: 300;
    line-height: 1.1;
  }
  .person-name .surname { font-weight: 700; }
  .person-title {
    font-size: 18px;
    font-weight: 700;
    color: var(--ink-white);
    letter-spacing: 0.5px;
    margin-top: 2px;
  }
  .phone-list {
    list-style: none;
    margin-top: 58px;
    font-size: 22px;
    line-height: 1.45;
  }
  .phone-label { font-weight: 700; color: var(--ink-white); }
  .phone-number { font-weight: 400; }
</style>
</head>
<body>
  <main class="stage">
    <article class="business-card">
      <svg class="card-shapes" viewBox="0 0 1050 600" preserveAspectRatio="none" aria-hidden="false">
        <polygon class="shape-black" points="525,0 1050,0 1050,270 788,480"></polygon>
        <polygon class="shape-cream" points="640,600 1050,600 1050,270"
                 role="img" aria-label="Faint city skyline illustration in cream tones"></polygon>
      </svg>

      <h1 class="brand-name">Ledgecrest Fix</h1>

      <section class="contact-block">
        <p class="person-name">Daniel <span class="surname">Trovato</span></p>
        <p class="person-title">PRESIDENT</p>
        <ul class="phone-list">
          <li><span class="phone-label">Office :</span> <span class="phone-number">(919)555-4827</span></li>
          <li><span class="phone-label">Mobile :</span> <span class="phone-number">(919)555-9306</span></li>
        </ul>
      </section>
    </article>
  </main>
</body>
</html>
```